Create Vertical Dog Food Labels (3 inches x 5 inches) for Pawlyn Kitchen

We need a packing Vertical label (3 inches x 5 inches) design for our line of Dog Food - Pawlyn Kitchen at pawlynkitchen.com (please review website). This design is for Custom Roll Labels. We have a logo already. Use our logo colors on label. What we need incorporated is a list of our ingredients:

50% Choice Beef
20% Pasture-raised Chicken
15% Brown Rice
15% Fresh Vegetables - Carrots, Kale, Zucchini
Herbal Health Boosters

We also need these lines at the bottom of the label:

Keeps in fridge for 4 days after thawing
Stores in freezer up to 6 months
Questions? email us at orders@brindlecopsepantry.com

We have attached a sample of a competitor. The Meadow Bowl.

Target Market(s)

Dog owners

Industry/Entity Type

Dog Food

Font styles to use
Sans Serif

Requirements
Must have
• Read project description above
Nice to have
• Our logo color incorporated
Should not have
• I want it simple.

```html
<!DOCTYPE html>
<html lang="en">
<head>
<meta charset="utf-8">
<title>Pawlyn Kitchen – Dog Food Label</title>
<link href="https://fonts.googleapis.com/css2?family=Poppins:wght@400;600;700&display=swap" rel="stylesheet">
<style>
  :root {
    --backdrop: #e8ebee;
    --label: #ffffff;
    --green-light: #86c144;
    --green-mid: #5ca445;
    --green-dark: #116b35;
    --yellow: #f6c042;
    --amber: #f6a21f;
    --orange: #f05f32;
    --rule: #8bc34a;
    --ink: #111111;
  }
  html, body {
    margin: 0;
    width: 1200px;
    height: 1000px;
    overflow: hidden;
    background: var(--backdrop);
    font-family: "Poppins", sans-serif;
  }
  .label {
    position: absolute;
    left: 364px;
    top: 105px;
    width: 474px;
    height: 790px;
    background: var(--label);
    box-shadow: 4px 5px 6px rgba(0,0,0,0.35);
  }
  .edge-bar {
    position: absolute;
    width: 16px;
  }
  .edge-bar.left { left: 0; }
  .edge-bar.right { right: 0; }
  .bar-top { top: 0; height: 252px; }
  .bar-middle { top: 267px; height: 250px; }
  .bar-bottom { top: 538px; height: 252px; }
  .left.bar-top { background: var(--green-light); }
  .left.bar-middle { background: var(--green-mid); }
  .left.bar-bottom { background: var(--green-dark); }
  .right.bar-top { background: var(--yellow); }
  .right.bar-middle { background: var(--amber); }
  .right.bar-bottom { background: var(--orange); }

  .brand-mark {
    position: absolute;
    left: 180px;
    top: 50px;
    width: 116px;
    height: 116px;
    border-radius: 50%;
    background: var(--green-light);
  }
  .brand-name {
    position: absolute;
    left: 0;
    right: 0;
    top: 196px;
    margin: 0;
    text-align: center;
    font-weight: 600;
    font-size: 42px;
    line-height: 56px;
    color: var(--green-dark);
    letter-spacing: 0.5px;
  }
  .ingredients, .care-info {
    position: absolute;
    margin: 0;
    font-size: 20px;
    line-height: 30px;
    color: var(--ink);
  }
  .ingredients { left: 56px; top: 276px; width: 400px; }
  .ingredients h2 {
    margin: 0;
    font-size: 20px;
    line-height: 30px;
    font-weight: 700;
  }
  .ingredients ul { list-style: none; margin: 0; padding: 0; }
  .divider {
    position: absolute;
    left: 33px;
    top: 527px;
    width: 411px;
    height: 2px;
    background: var(--rule);
  }
  .care-info { left: 61px; top: 568px; width: 380px; }
  .care-info p { margin: 0; }
  .care-info strong { font-weight: 700; }
</style>
</head>
<body>
  <section class="label">
    <div class="edge-bar left bar-top"></div>
    <div class="edge-bar left bar-middle"></div>
    <div class="edge-bar left bar-bottom"></div>
    <div class="edge-bar right bar-top"></div>
    <div class="edge-bar right bar-middle"></div>
    <div class="edge-bar right bar-bottom"></div>

    <div class="brand-mark"></div>
    <h1 class="brand-name">Pawlyn Kitchen</h1>

    <div class="ingredients">
      <h2>Ingredients:</h2>
      <ul>
        <li>50% Choice Beef</li>
        <li>20% Pasture-raised Chicken</li>
        <li>15% Brown Rice</li>
        <li>15% Fresh Vegetables - Carrots, Kale, Zucchini</li>
        <li>Herbal Health Boosters</li>
      </ul>
    </div>

    <div class="divider"></div>

    <div class="care-info">
      <p><strong>Keeps</strong> in fridge for 4 days after thawing</p>
      <p><strong>Stores</strong> in freezer up to 6 months</p>
      <p><strong>Questions?</strong></p>
      <p>email us at</p>
      <p>orders@brindlecopsepantry.com</p>
    </div>
  </section>
</body>
</html>
```